Business Card Needed for Crafter of Pottery, Jewelry and Artwork

Calling all designers in search of an artistic challenge.

I need a new business card design for my pottery, jewelry and artwork business, Woven Glass and Tide, based in Vancouver BC.

I would like a card that is bright and inviting and preferably incorporates my logo and a sample of photos of my work while having a clean fresh look. The following contact details would preferably be included on the card as well:
• Melinda Osgood
• Designer
• Phone: 604.555.0147
• Email: Designer@WovenGlassandTide.example
• Website: www.WovenGlassandTide.example
• Blog: www.KilnNotesDaily.example

The logo is attached in two color schemes in both Vector and Source formats. On past cards I’ve also included photos of my work. By including photos of the work the pieces are showcased and it catches people’s eye and prompts them to pick up the card and look at it more closely. For example, if I leave a stack in a coffee shop I want people to be drawn to the card, to pick it up and get a sense of the my product lines. Please feel free to pull photos of my work directly off of my website. If you need photos with higher pixels please let me know and I’ll email them directly to you. The website background is bffbda (191, 251, 218). I would like the business cards to match the feel of the website for consistency but the cards do not need to use the exact same colors. My website and current business card are predominantly turquoise shades. The background uses stripes provided by the website template. I don’t know the exact colors of the stripes.

My current business card is attached to show the use of photos in a design. Please note that I am not thrilled with my own design and am looking for variations and completely new designs. This example is not meant to be used as a template or starting point.

Here is some background surrounding my company:
WGT offers one of a kind jewelry, pottery, artwork and leather bags each designed with a twist. The pottery varies from rustic every day functional ware to raku artwork. The jewelry ranges from simple sterling every day pieces to multimedia pieces incorporating stone, metal, ceramics and fabric. The artwork is multimedia, typically acrylic paired with a natural element such as bark. All the bags are leather with reworked kimono fabric or patterned silk lining.

Feel free to check out my website to get a flavour for my work and the color scheme I've used on marketing materials so far. www.wovenglassandtide.example
Updates

Thank you to everyone who has submitted a design so far. I hope everyone has received some helpful feedback.

I'm going to post a survey to customers and friends asking for their votes. If you have new designs to submit please try to get them in by Saturday March 30 at noon so that I can include it in the survey launch.

Thank you

Target Market(s)

Females aged 25-65 interested in one of a kind functional pottery and jewelry.

Industry/Entity Type

Coffee Shop

Requirements
Must have
• Contact information, website, blog
Nice to have
• Logo, photos

```html
<!DOCTYPE html>
<html lang="en">
<head>
<meta charset="utf-8">
<title>Woven Glass and Tide — Business Card</title>
<link rel="stylesheet" href="https://fonts.googleapis.com/css2?family=Marcellus+SC&display=swap">
<style>
  :root {
    --teal: #1fb5a8;
    --teal-soft: #5fcfc4;
    --paper: #fdfdfb;
    --backdrop: #e6e6e3;
    --clay-light: #eeeeea;
    --clay-mid: #cfcfc8;
    --stone-sky: #e9e9ee;
    --bead-red: #d8503f;
    --bead-navy: #2b3b6a;
    --burlap: #b9b7ad;
    --bead-aqua: #bfe9e4;
    --bead-pink: #e99ab4;
  }
  * { box-sizing: border-box; margin: 0; padding: 0; }
  html, body { width: 742px; height: 1200px; overflow: hidden; }
  body {
    background: var(--backdrop);
    font-family: "Marcellus SC", serif;
    color: var(--teal);
    position: relative;
  }
  .card {
    position: absolute;
    left: 51px;
    width: 640px;
    height: 366px;
    background: var(--paper);
    box-shadow: 0 6px 18px rgba(0,0,0,.18);
    overflow: hidden;
  }
  .card--front { top: 204px; }
  .card--back { top: 630px; }

  /* Brand mark: name inside a plain ring */
  .brand {
    position: absolute;
    border: 3px solid var(--teal);
    border-radius: 50%;
    display: flex;
    align-items: center;
    justify-content: center;
    text-align: center;
    background: var(--paper);
  }
  .brand__name {
    font-size: 19px;
    line-height: 1.15;
    letter-spacing: 1px;
    color: var(--teal);
  }
  .card--front .brand { left: 412px; top: 14px; width: 150px; height: 150px; }
  .card--back .brand { left: 120px; top: 244px; width: 112px; height: 112px; z-index: 2; }
  .card--back .brand__name { font-size: 14px; }

  .web-links {
    position: absolute;
    left: 30px;
    top: 32px;
    list-style: none;
    font-size: 14px;
    line-height: 24px;
  }
  .web-links li, .contact { display: flex; align-items: center; gap: 8px; }
  .icon { width: 14px; height: 14px; flex: none; }

  .person {
    position: absolute;
    left: 150px;
    top: 170px;
  }
  .person__name {
    font-size: 40px;
    font-weight: 400;
    letter-spacing: 2px;
    line-height: 1;
  }
  .person__role {
    font-size: 20px;
    color: var(--teal-soft);
    margin-left: 70px;
    margin-top: 2px;
    letter-spacing: 1px;
  }

  .dots {
    position: absolute;
    display: flex;
    gap: 12px;
  }
  .dots span {
    width: 4px; height: 4px; border-radius: 50%;
    background: var(--teal);
  }
  .card--front .dots { left: 44px; top: 292px; }
  .card--back .dots { left: 40px; top: 340px; }

  .contact { position: absolute; font-size: 15px; }
  .contact--email { left: 230px; top: 286px; }
  .contact--phone { left: 460px; top: 322px; }

  /* Back side photo panels */
  .photo { position: absolute; }
  .photo--pottery {
    left: 0; top: 0; width: 210px; height: 210px;
    background: radial-gradient(ellipse at 45% 60%, var(--clay-light), var(--clay-mid) 70%, #e2e2dd);
  }
  .photo--earrings {
    left: 210px; top: 0; width: 230px; height: 210px;
    background: radial-gradient(circle at 55% 60%, rgba(216,80,63,.45), transparent 30%),
                radial-gradient(circle at 65% 45%, rgba(43,59,106,.4), transparent 25%),
                var(--stone-sky);
  }
  .photo--beads {
    left: 440px; top: 0; width: 200px; height: 300px;
    background: radial-gradient(circle at 50% 65%, var(--bead-aqua), rgba(233,154,180,.6) 30%, transparent 55%),
                var(--burlap);
  }
  .divider { position: absolute; background: var(--teal); }
  .divider--v1 { left: 209px; top: 0; width: 2px; height: 210px; }
  .divider--v2 { left: 439px; top: 0; width: 2px; height: 300px; }
  .divider--h1 { left: 0; top: 209px; width: 440px; height: 2px; }
  .divider--h2 { left: 440px; top: 299px; width: 200px; height: 2px; }
</style>
</head>
<body>

<section class="card card--front" aria-label="Business card front">
  <div class="brand"><span class="brand__name">Woven Glass<br>and Tide</span></div>

  <ul class="web-links">
    <li>
      <svg class="icon" viewBox="0 0 14 14" aria-hidden="true"><circle cx="7" cy="7" r="6" fill="none" stroke="currentColor" stroke-width="1.3"/><ellipse cx="7" cy="7" rx="2.6" ry="6" fill="none" stroke="currentColor" stroke-width="1"/><line x1="1" y1="7" x2="13" y2="7" stroke="currentColor" stroke-width="1"/></svg>
      www.WovenGlassandTide.example
    </li>
    <li>
      <svg class="icon" viewBox="0 0 14 14" aria-hidden="true"><circle cx="7" cy="7" r="6" fill="none" stroke="currentColor" stroke-width="1.3"/><ellipse cx="7" cy="7" rx="2.6" ry="6" fill="none" stroke="currentColor" stroke-width="1"/><line x1="1" y1="7" x2="13" y2="7" stroke="currentColor" stroke-width="1"/></svg>
      www.KilnNotesDaily.example
    </li>
  </ul>

  <div class="person">
    <h1 class="person__name">Melinda Osgood</h1>
    <p class="person__role">Designer</p>
  </div>

  <div class="dots" aria-hidden="true"><span></span><span></span><span></span></div>

  <p class="contact contact--email">
    <svg class="icon" viewBox="0 0 14 14" aria-hidden="true"><rect x="1" y="3" width="12" height="8" fill="currentColor"/><polyline points="1,3 7,8 13,3" fill="none" stroke="#fff" stroke-width="1.1"/></svg>
    Designer@WovenGlassandTide.example
  </p>
  <p class="contact contact--phone">
    <svg class="icon" viewBox="0 0 14 14" aria-hidden="true"><rect x="3.5" y="1" width="7" height="12" rx="1.2" fill="none" stroke="currentColor" stroke-width="1.3"/><circle cx="7" cy="11" r=".8" fill="currentColor"/></svg>
    604.555.0147
  </p>
</section>

<section class="card card--back" aria-label="Business card back">
  <div class="photo photo--pottery" role="img" aria-label="Photo of two cream glazed pottery jars"></div>
  <div class="photo photo--earrings" role="img" aria-label="Photo of red, navy and purple bead earrings hanging from a branch"></div>
  <div class="photo photo--beads" role="img" aria-label="Photo of aqua and pink bead cluster earrings on burlap"></div>
  <div class="divider divider--v1"></div>
  <div class="divider divider--v2"></div>
  <div class="divider divider--h1"></div>
  <div class="divider divider--h2"></div>

  <div class="brand"><span class="brand__name">Woven Glass<br>and Tide</span></div>
  <div class="dots" aria-hidden="true"><span></span><span></span><span></span></div>
</section>

</body>
</html>
```